Visitenkarte erstellen für Reiki Praxis

Visitenkarten für Reiki Praxis Doppelseitig

business cards reiki practice double-sided

The background can also be a different color

```html
<!DOCTYPE html>
<html lang="de">
<head>
<meta charset="utf-8">
<title>Lumen Vita – Visitenkarte</title>
<link rel="stylesheet" href="https://fonts.googleapis.com/css2?family=Jost:wght@300;400&display=swap">
<style>
  :root {
    --page: #e4e5e7;
    --rose: #b85c84;
    --sage: #9a9a86;
    --sand: #b9a07e;
    --peach: #f4a66f;
    --ink: #141414;
    --white: #ffffff;
    --brand-gradient: linear-gradient(90deg, var(--rose) 0%, var(--sage) 40%, var(--sand) 62%, var(--peach) 100%);
  }
  * { box-sizing: border-box; margin: 0; padding: 0; }
  html, body {
    width: 1200px; height: 1200px; overflow: hidden;
    background: var(--page);
    font-family: "Jost", sans-serif;
  }
  .card {
    position: absolute; left: 198px; width: 804px; height: 520px;
    box-shadow: 0 10px 30px rgba(0,0,0,0.18);
  }
  .card--front { top: 40px; background: var(--brand-gradient); }
  .card--back { top: 626px; background: var(--ink); overflow: hidden; }

  .brand-mark {
    position: absolute; border-radius: 50%;
    border: 2px solid var(--white);
  }
  .card--front .brand-mark { width: 90px; height: 90px; left: 357px; top: 150px; }
  .brand-name {
    position: absolute; left: 0; width: 100%; text-align: center;
    font-weight: 400; color: var(--white); letter-spacing: 0.04em; white-space: nowrap;
  }
  .card--front .brand-name { top: 282px; font-size: 50px; }

  .card--back .brand-mark { width: 62px; height: 62px; left: 215px; top: 62px; border-color: var(--sand); }
  .card--back .brand-name { left: 66px; width: 360px; top: 150px; font-size: 31px; }

  .holder { position: absolute; right: 74px; text-align: right; }
  .holder__name {
    top: 224px; font-size: 30px; font-weight: 400; letter-spacing: 0.02em;
    background: var(--brand-gradient); -webkit-background-clip: text; background-clip: text; color: transparent;
  }
  .holder__role { top: 264px; font-size: 21px; font-weight: 400; color: var(--white); }

  .divider {
    position: absolute; left: 72px; top: 303px; width: 658px; height: 2px;
    background: var(--brand-gradient);
  }
  .contact-list { position: absolute; left: 72px; top: 318px; list-style: none; }
  .contact-list li {
    display: flex; align-items: center; height: 37.5px;
    font-size: 20px; font-weight: 300; color: var(--white); letter-spacing: 0.02em;
  }
  .contact-list svg { width: 24px; height: 24px; margin-right: 19px; flex: none; }

  .accent-band {
    position: absolute; left: 0; bottom: 0; width: 100%; height: 42px;
    background: var(--brand-gradient);
  }
</style>
</head>
<body>
  <section class="card card--front">
    <div class="brand-mark"></div>
    <div class="brand-name">LUMEN VITA</div>
  </section>

  <section class="card card--back">
    <div class="brand-mark"></div>
    <div class="brand-name">LUMEN VITA</div>

    <div class="holder holder__name">MARA LENZ</div>
    <div class="holder holder__role">Eigentümer</div>

    <div class="divider"></div>

    <ul class="contact-list">
      <li>
        <svg viewBox="0 0 24 24" aria-hidden="true"><path fill="#c98a78" d="M6.6 10.8a15.1 15.1 0 0 0 6.6 6.6l2.2-2.2c.3-.3.7-.4 1-.2 1.1.4 2.3.6 3.6.6.6 0 1 .4 1 1V20c0 .6-.4 1-1 1A17 17 0 0 1 3 4c0-.6.4-1 1-1h3.5c.6 0 1 .4 1 1 0 1.3.2 2.5.6 3.6.1.3 0 .7-.2 1z"/></svg>
        123456789
      </li>
      <li>
        <svg viewBox="0 0 24 24" aria-hidden="true"><rect x="2" y="5" width="20" height="14" fill="#d49a7c"/><path d="M2 5l10 8 10-8M2 19l7-7M22 19l-7-7" fill="none" stroke="#141414" stroke-width="1.6"/></svg>
        info@lumenvita.com
      </li>
      <li>
        <svg viewBox="0 0 24 24" aria-hidden="true"><g fill="none" stroke="#b98a82" stroke-width="1.6"><circle cx="12" cy="12" r="9.5"/><ellipse cx="12" cy="12" rx="4.5" ry="9.5"/><path d="M2.5 12h19M4 7h16M4 17h16"/></g></svg>
        www.lumenvita.com
      </li>
      <li>
        <svg viewBox="0 0 24 24" aria-hidden="true"><path fill="#c9a07e" d="M12 2a7 7 0 0 0-7 7c0 5 7 13 7 13s7-8 7-13a7 7 0 0 0-7-7zm0 9.5A2.5 2.5 0 1 1 12 6.5a2.5 2.5 0 0 1 0 5z"/></svg>
        Name Ihrer Region, Stadt, Deutschland 12345
      </li>
    </ul>

    <div class="accent-band"></div>
  </section>
</body>
</html>
```